Banner for homepage

It is a new banner for the homepage, temporary site address is 203.0.113.57 ( is the biggest banner only ) . Would be 5 variations for image content as below (in Portuguese ) :

Image 1:
Leitor de codigo de barras
Todos os tipos de leitores de código de barras para as mais diversas aplicações.
( example of product images in : http://www.quorvelidx.com/en-US/Pages/Category.aspx?category=barcode-scanners&cat=QMT)

Image 2:
Impressora de etiquetas
Identifique o que for nessário com o melhor custo/beneficio e flexibilidade de materiais de impressão.
( example of product images in : tarnix.com in label printers desktop and industrial)

Image 3:
Impressora de cupom
Imprima recibos e cupons fiscais com agilidade e qualidade, temos a impressora certa para o seu PDV.
( example of product images in : http://www.plivorato.com.br/equipamento-categoria-impressoras+fiscais.html)

Image 4:
Coletor de dados
Computadores móveis com leitor de código de barras, que levam a automação para frente de trabalho.
( example of product images in : http://www.quorvelidx.com/en-US/Pages/Category.aspx?cat=QMT&category=hand-held-mobile-computer)

Image 5:
Etiquetas e Ribbons:
Etiquetas adesivas e não adesivas em vários de tipos de materiais, papéis e plásticos. O ribbon certo para impressão perfeita em cada material.
( example of product images in : http://www.lumetrask.com/cats/supplies/barcode-printer.htm?nav=hdr)

```html
<!DOCTYPE html>
<html lang="pt">
<head>
<meta charset="utf-8">
<title>Banners para homepage</title>
<link href="https://fonts.googleapis.com/css2?family=Roboto+Condensed:wght@400;700&family=Arimo:wght@400&display=swap" rel="stylesheet">
<style>
  :root{
    --navy:#3c4566;
    --navy-light:#4d5679;
    --navy-dark:#323a58;
    --band:#343c5b;
    --paper:#f3f3f5;
    --paper-shade:#dcdde4;
    --orange:#f7a600;
    --orange-edge:#ffd16b;
    --tag-bg:#e9e9ec;
    --tag-text:#3a3a3a;
    --meta:#8a8a8a;
    --white:#ffffff;
    --product:#b9bcc6;
    --product-dark:#2b2e36;
  }
  *{margin:0;padding:0;box-sizing:border-box}
  html,body{width:1200px;height:2674px;overflow:hidden;background:var(--white)}
  body{position:relative;font-family:"Arimo",Arial,sans-serif}
  .meta{position:absolute;left:84px;top:156px;font-family:"Roboto Condensed",sans-serif;color:var(--meta);font-size:27px;line-height:34px;text-transform:uppercase}
  .banner{position:absolute;left:84px;width:1026px;height:468px;overflow:hidden}
  .banner svg.bg{position:absolute;inset:0}
  .tag{position:absolute;right:0;top:0;width:134px;height:48px;background:var(--tag-bg);color:var(--tag-text);font-family:"Roboto Condensed",sans-serif;font-weight:700;font-size:22px;line-height:48px;text-align:center}
  .title{position:absolute;font-family:"Roboto Condensed",sans-serif;font-weight:700;font-size:42px;line-height:48px;text-transform:uppercase;color:var(--white);white-space:nowrap}
  .copy{position:absolute;font-size:21px;line-height:29px;color:var(--white)}
  .btn{position:absolute;width:180px;height:32px;background:var(--orange);border:2px solid var(--orange-edge);color:var(--white);font-size:20px;line-height:28px;padding-left:14px;letter-spacing:.5px}
  .btn svg{vertical-align:middle;margin-left:6px}
  .light .title{color:var(--navy)}
  .light .copy{color:#333}
  .product{position:absolute;border-radius:24px}
  .b1{top:270px;background:var(--navy)}
  .b2{top:750px;background:var(--navy)}
  .b3{top:1230px;background:var(--paper)}
  .b4{top:1710px;background:var(--paper)}
  .b5{top:2190px;background:var(--navy)}
  .band{position:absolute;left:0;background:var(--band)}
</style>
</head>
<body>
  <div class="meta">Banner ads for 203.0.113.57<br>Banner for homepage</div>

  <section class="banner b1">
    <svg class="bg" width="1026" height="468"><polygon points="600,0 1026,0 1026,468 380,468" fill="var(--navy-light)"/><polygon points="0,330 560,330 500,468 0,468" fill="var(--navy-dark)" opacity=".5"/></svg>
    <div class="product" role="img" aria-label="Leitores de código de barras manuais e de base" style="left:540px;top:10px;width:486px;height:458px;background:linear-gradient(135deg,#d9dbe0 0%,#5c606b 55%,#2b2e36 100%)"></div>
    <div class="tag">BANNER1</div>
    <h2 class="title" style="left:26px;top:188px">Leitor de codigo de barras</h2>
    <p class="copy" style="left:26px;top:244px;width:560px">Todos os tipos de leitores de código de barras para as mais diversas aplicações.</p>
    <div class="btn" style="left:26px;top:324px">VEJA MAIS<svg width="10" height="12"><polygon points="0,0 10,6 0,12" fill="#fff"/></svg></div>
  </section>

  <section class="banner b2">
    <svg class="bg" width="1026" height="468"><polygon points="620,0 1026,0 1026,468 460,468" fill="var(--navy-light)"/><polygon points="0,300 640,300 600,380 0,380" fill="var(--navy-dark)" opacity=".5"/></svg>
    <div class="product" role="img" aria-label="Impressora industrial de etiquetas" style="left:626px;top:50px;width:380px;height:390px;border-radius:6px;background:linear-gradient(160deg,#d8d8cf 0%,#a9a9a0 60%,#77776f 100%)"></div>
    <div class="tag">BANNER2</div>
    <h2 class="title" style="left:40px;top:146px">Impressora de etiquetas</h2>
    <p class="copy" style="left:40px;top:204px;width:500px">Identifique o que for nessário com o melhor custo/beneficio e flexibilidade de materiais de impressão.</p>
    <div class="btn" style="left:40px;top:324px">VEJA MAIS<svg width="10" height="12"><polygon points="0,0 10,6 0,12" fill="#fff"/></svg></div>
  </section>

  <section class="banner b3 light">
    <svg class="bg" width="1026" height="468"><polygon points="760,0 1026,0 1026,468 500,468" fill="var(--paper-shade)"/></svg>
    <div class="product" role="img" aria-label="Duas impressoras de cupom fiscal pretas" style="left:526px;top:60px;width:480px;height:380px;background:linear-gradient(150deg,#55585f 0%,#2b2d33 60%,#1a1b1f 100%)"></div>
    <div class="tag">BANNER3</div>
    <h2 class="title" style="left:40px;top:142px">Impressora de cupom</h2>
    <p class="copy" style="left:40px;top:198px;width:470px">Imprima recibos e cupons fiscais com agilidade e qualidade, temos a impressora certa para o seu PDV.</p>
    <div class="btn" style="left:40px;top:306px">VEJA MAIS</div>
  </section>

  <section class="banner b4 light">
    <svg class="bg" width="1026" height="468"><polygon points="720,0 1026,0 1026,468 500,468" fill="var(--paper-shade)"/></svg>
    <div class="band" style="top:196px;width:640px;height:96px"></div>
    <div class="product" role="img" aria-label="Três coletores de dados portáteis com tela e teclado" style="left:552px;top:30px;width:454px;height:380px;background:linear-gradient(120deg,#3a3d45 0%,#1f2126 50%,#4a4d56 100%)"></div>
    <div class="tag">BANNER4</div>
    <h2 class="title" style="left:26px;top:144px">Coletor de dados</h2>
    <p class="copy" style="left:26px;top:200px;width:520px;color:var(--white)">Computadores móveis com leitor de código de barras, que levam a automação para frente de trabalho.</p>
    <div class="btn" style="left:26px;top:312px">VEJA MAIS<svg width="10" height="12"><polygon points="0,0 10,6 0,12" fill="#fff"/></svg></div>
  </section>

  <section class="banner b5">
    <svg class="bg" width="1026" height="468"><polygon points="800,0 1026,0 1026,200 720,200" fill="var(--navy-light)"/></svg>
    <div class="band" style="top:90px;width:820px;height:64px"></div>
    <div class="product" role="img" aria-label="Ribbon de impressão, cabeça de impressão e rolo de ribbon" style="left:6px;top:200px;width:740px;height:268px;background:linear-gradient(90deg,#2f8f86 0%,#9ea3ab 45%,#e6e6e6 75%,#2a2a2a 100%)"></div>
    <div class="product" role="img" aria-label="Rolos de etiquetas adesivas brancas" style="left:746px;top:140px;width:270px;height:328px;background:linear-gradient(160deg,#ffffff 0%,#e2e3e8 60%,#c5c8d2 100%)"></div>
    <div class="tag">BANNER5</div>
    <h2 class="title" style="left:40px;top:22px">Etiquetas e ribbons:</h2>
    <p class="copy" style="left:40px;top:92px;width:800px;font-size:18px;line-height:28px">Etiquetas adesivas e não adesivas em vários de tipos de materiais, papéis e plásticos. O ribbon certo para impressão perfeita em cada material.</p>
    <div class="btn" style="left:40px;top:182px">VEJA MAIS<svg width="10" height="12"><polygon points="0,0 10,6 0,12" fill="#fff"/></svg></div>
  </section>
</body>
</html>
```